Etiketten-Design für Getränkedose
Zielgruppe
Ich werde Getränke in Dosen 250 ml herstellen lassen, welches ich im Markt vertreiben möchte.
Aufgabenstellung
Das Pfandlogo und die EAN müssen an die Etiketten rangebracht werden, deshalb ist es wichtig, dass wenn Sie keine Möglichkeit haben die EAN ranzubringen, dass Platz im Design frei gehalten wird.
Im Anhang 1 finden Sie die Abmessungen von den Etiketten die an die Dosen rangebracht werden sollen!
Das Design muss innerhalb von diesen Abmessungen erstellt werden.
Es handelt sich hier nur um eine Druckvorlage!
Für so eine Druckvorlage muss auf den Etiketten Platz frei gehalten werden.
Ich benötige von Ihnen 3D Dosendesigns, sowie in meiner Skizze.
Wichtig: Es sollen auschließlich die Farben Weiß und Grün genutzt werden.
Meine Marke heißt ' Silver Quince' und es ist wichtig, dass die Farbe grün mit der Limette von meinem Logo passt.
Anhang 2&3= Mein Logo
Anhang 4= Eine Skizze von mir.
Ganz oben am Dosenrand soll das Wort Lemon in Grün NICHT mit eingeführt werden.
Ganz unten soll bitte in Farbe Grau die Zahl: (2018) auf Römisch hinzugefügt werden und das Grau und die Schrift soll bitte mit meinem Logo passen:
MMXVIII
Wichtig: Es soll ein edles und modernes Design werden!
Ich freue mich auf Ihre kreativen Designs.
Als Vorgabe: Die Dose soll weiß sein und es sollen grüne Farben benutzt werden und es soll mit dem Logo farblich übereinstimmen.
Vielen Dank im Voraus

```html
<!DOCTYPE html>
<html lang="de">
<head>
<meta charset="utf-8">
<title>Silver Quince – Dosenetikett</title>
<link rel="stylesheet" href="https://fonts.googleapis.com/css2?family=Tenor+Sans&display=swap">
<style>
  :root {
    --paper: #f3f4f3;
    --paper-white: #fbfcfb;
    --mint-fade: #dcffc4;
    --lime-soft: #b4ff78;
    --lime: #80ff14;
    --lime-mark: #4cf01a;
    --slate: #4e5658;
  }
  html, body {
    margin: 0;
    padding: 0;
    width: 1200px;
    height: 896px;
    overflow: hidden;
  }
  .label {
    position: relative;
    width: 1200px;
    height: 896px;
    overflow: hidden;
    font-family: "Tenor Sans", sans-serif;
    color: var(--slate);
  }
  .label__backdrop {
    position: absolute;
    inset: 0;
    background: linear-gradient(
      to bottom,
      var(--paper) 0px,
      var(--paper-white) 390px,
      var(--mint-fade) 470px,
      var(--lime-soft) 580px,
      var(--lime) 740px,
      var(--lime) 896px
    );
  }
  .brand {
    position: absolute;
    left: 606px;
    top: 352px;
    display: flex;
    align-items: center;
    gap: 22px;
  }
  .brand__name {
    margin: 0;
    font-weight: 400;
    font-size: 36px;
    line-height: 40px;
    letter-spacing: 0.18em;
    text-transform: uppercase;
    color: var(--slate);
  }
  .brand__dot {
    width: 90px;
    height: 90px;
    border-radius: 50%;
    background: var(--lime-mark);
  }
  .year {
    position: absolute;
    left: 706px;
    top: 782px;
    margin: 0;
    font-weight: 400;
    font-size: 43px;
    line-height: 48px;
    letter-spacing: 0.01em;
    color: var(--slate);
  }
</style>
</head>
<body>
  <main class="label">
    <div class="label__backdrop" role="img" aria-label="Zartes weißes Damastmuster mit Ranken, das nach unten in einen limettengrünen Verlauf übergeht"></div>

    <div class="brand">
      <p class="brand__name">Silver<br>Quince</p>
      <span class="brand__dot" aria-hidden="true"></span>
    </div>

    <p class="year">MMXVIII</p>
  </main>
</body>
</html>
```